My Web Development Portfolio site

I'm a web developer and I need a web design that can showcase my web development portfolio. I like most of the websites from this link: http://www.mintquarry.example/galleries/samples-493051. My ideal design should be modern, clean and fun. I will let the designer decided the color theme for the website.

Target Market(s)

Potential Employers.

Number of Pages Required

1 page

Requirements
Must have
• - Menu bar that includes at least: About Me, Blog, Contact, Project/Work
• - Excellent color theme
• - Use the logo I provided (see attachment)
Nice to have
• - Some animation
• - Fun yet modern design

```html
<!DOCTYPE html>
<html lang="en">
<head>
<meta charset="utf-8">
<title>Byte Trail – Web Development Portfolio</title>
<link href="https://fonts.googleapis.com/css2?family=Raleway:wght@300;400;500;600&family=Open+Sans:wght@400;600&display=swap" rel="stylesheet">
<style>
  :root {
    --orange: #f47a3c;
    --orange-light: #f9a062;
    --orange-deep: #e8622a;
    --white: #ffffff;
    --ink: #333333;
    --grey-text: #777777;
    --band-grey: #6f6f6f;
    --contact-bg: #2a2a2a;
    --footer-bg: #141414;
    --line: #bdbdbd;
  }
  * { box-sizing: border-box; margin: 0; padding: 0; }
  html, body { width: 1200px; height: 2230px; overflow: hidden; }
  body {
    position: relative;
    background: var(--white);
    font-family: "Open Sans", Arial, sans-serif;
    color: var(--ink);
  }
  .abs { position: absolute; }

  /* Hero */
  .hero {
    position: absolute; left: 0; top: 0; width: 1200px; height: 630px;
    background: linear-gradient(180deg, var(--orange-light) 0%, var(--orange) 45%, var(--orange-deep) 100%);
  }
  .hero-scene {
    position: absolute; left: 215px; top: 345px; width: 775px; height: 285px;
    background: linear-gradient(180deg, rgba(255,255,255,0.10), rgba(60,30,20,0.18));
    border-radius: 6px 6px 0 0;
  }
  .brand {
    position: absolute; left: 176px; top: 70px;
    display: flex; align-items: center; gap: 14px;
    font-family: "Raleway", Arial, sans-serif; font-weight: 300;
    font-size: 40px; color: var(--white); letter-spacing: 1px;
  }
  .brand-dot { width: 22px; height: 22px; border-radius: 50%; background: var(--white); }
  .main-nav {
    position: absolute; left: 566px; top: 48px;
    display: flex; gap: 38px;
    font-family: "Raleway", Arial, sans-serif; font-size: 14px; font-weight: 500;
    color: var(--white); letter-spacing: 0.3px;
  }
  .main-nav a { color: inherit; text-decoration: none; }
  .hero-title {
    position: absolute; left: 0; top: 188px; width: 1200px; text-align: center;
    font-family: "Raleway", Arial, sans-serif; font-weight: 400; color: var(--white);
    line-height: 1.1;
  }
  .hero-title .line-1 { display: block; font-size: 50px; }
  .hero-title .line-2 { display: block; font-size: 38px; margin-top: 4px; }
  .slide-arrow { position: absolute; width: 22px; height: 34px; }

  /* About */
  .section-mark {
    position: absolute; width: 26px; height: 26px; border-radius: 50%;
    border: 3px solid var(--ink);
  }
  .portrait {
    position: absolute; left: 232px; top: 700px; width: 252px; height: 252px;
    border-radius: 50%; border: 2px solid var(--orange); padding: 6px;
  }
  .portrait-fill {
    width: 100%; height: 100%; border-radius: 50%;
    background: radial-gradient(circle at 50% 40%, #d9b9a0 0%, #8a6a55 55%, #2b2522 100%);
  }
  .about-heading {
    position: absolute; left: 512px; top: 718px;
    font-family: "Raleway", Arial, sans-serif; font-weight: 400; font-size: 38px; color: var(--ink);
  }
  .about-text {
    position: absolute; left: 512px; width: 525px;
    font-size: 12px; line-height: 22px; color: var(--grey-text);
  }

  /* Projects */
  .projects {
    position: absolute; left: 0; top: 1043px; width: 1200px; height: 380px;
    background: linear-gradient(135deg, #8a8a8a 0%, var(--band-grey) 50%, #5a5a5a 100%);
  }
  .projects-tab {
    position: absolute; left: 565px; top: 1018px; width: 70px; height: 52px;
    background: var(--white); border-radius: 35px 35px 0 0;
  }
  .projects-tab-mark {
    position: absolute; left: 588px; top: 1030px; width: 24px; height: 24px;
    border-radius: 50%; border: 3px solid var(--orange);
  }
  .projects-heading {
    position: absolute; left: 0; top: 1077px; width: 1200px; text-align: center;
    font-family: "Raleway", Arial, sans-serif; font-size: 27px; color: var(--white); font-weight: 500;
  }
  .project-row { position: absolute; left: 195px; top: 1133px; }

  /* Blogs */
  .blogs-heading {
    position: absolute; left: 0; top: 1466px; width: 1200px; text-align: center;
    font-family: "Raleway", Arial, sans-serif; font-size: 28px; color: var(--orange); font-weight: 400;
  }
  .blog-post { position: absolute; top: 1545px; width: 268px; }
  .blog-title {
    font-family: "Raleway", Arial, sans-serif; font-size: 15.5px; line-height: 19px;
    color: var(--ink); font-weight: 500;
  }
  .blog-excerpt { margin-top: 13px; font-size: 11px; line-height: 18px; color: var(--grey-text); }
  .blog-date { margin-top: 7px; font-size: 12px; color: var(--ink); }

  /* Contact */
  .contact {
    position: absolute; left: 0; top: 1798px; width: 1200px; height: 375px;
    background: var(--contact-bg);
  }
  .contact-heading {
    position: absolute; left: 0; top: 1847px; width: 1200px; text-align: center;
    font-family: "Raleway", Arial, sans-serif; font-size: 26px; color: var(--white); font-weight: 500;
  }
  .field {
    position: absolute; left: 253px; width: 369px;
    border: 1px solid var(--line); color: var(--white);
    font-size: 10px; letter-spacing: 0.3px; padding: 8px 14px;
  }
  .submit-button {
    position: absolute; left: 253px; top: 2071px; width: 91px; height: 34px;
    background: var(--orange); color: var(--white);
    font-size: 11px; font-weight: 600; letter-spacing: 0.5px;
    display: flex; align-items: center; justify-content: center;
  }
  .contact-line {
    position: absolute; left: 703px; display: flex; gap: 6px; align-items: flex-start;
    font-size: 13px; line-height: 19px; color: var(--white);
  }
  .contact-line svg { flex: none; margin-top: 2px; }
  .social-row { position: absolute; left: 702px; top: 2026px; display: flex; gap: 5px; }
  .social-circle { width: 28px; height: 28px; border-radius: 50%; border: 1.5px solid var(--white); }

  /* Footer */
  .site-footer {
    position: absolute; left: 0; top: 2173px; width: 1200px; height: 57px;
    background: var(--footer-bg);
  }
  .footer-note {
    position: absolute; left: 181px; top: 2195px;
    font-size: 10px; color: #8a8a8a;
  }
</style>
</head>
<body>

  <!-- Hero -->
  <header class="hero" role="img" aria-label="Orange sunset landscape illustration with hills and trees behind a developer desk"></header>
  <div class="hero-scene" role="img" aria-label="Illustrated desk with a monitor showing code, notepad, glasses, cactus, phone, envelope and tea cup"></div>

  <div class="brand"><span class="brand-dot"></span>bytetrail</div>

  <nav class="main-nav">
    <a href="#">HOME</a>
    <a href="#">ABOUT ME</a>
    <a href="#">BLOG</a>
    <a href="#">PROJECT/WORK</a>
    <a href="#">CONTACT</a>
  </nav>

  <h1 class="hero-title">
    <span class="line-1">HI.. WELCOME TO</span>
    <span class="line-2">BYTE TRAIL</span>
  </h1>

  <svg class="slide-arrow" style="left:135px;top:260px" viewBox="0 0 22 34"><polyline points="18,3 5,17 18,31" fill="none" stroke="#ffffff" stroke-width="4"/></svg>
  <svg class="slide-arrow" style="left:1045px;top:260px" viewBox="0 0 22 34"><polyline points="4,3 17,17 4,31" fill="none" stroke="#ffffff" stroke-width="4"/></svg>

  <!-- About -->
  <section>
    <div class="section-mark" style="left:576px;top:678px"></div>
    <div class="portrait"><div class="portrait-fill" role="img" aria-label="Portrait photo of the developer"></div></div>
    <h2 class="about-heading">About Me</h2>
    <p class="about-text" style="top:780px">Avestibulum volutpat imperdiet ac nisl Cum sociis natoque penatibus et magnis dis parturient montes nascetur ridiculus mus In iaculis facilisis</p>
    <p class="about-text" style="top:834px">Maecenas aliquet velit vel turpis Mauris neque metus malesuada nec ultricies sit amet porttitor mattis enim In massa libero interdum nec interdum vel blandit sed nulla In ullamcorper est eget tempor cursus neque mi consectetuer mi a ultricies massa est sed nisl at justo id velit placerat molestie Donec dictum lectus non odio Cras a ante vitae enim iaculis aliquam Mauris nunc quamv</p>
  </section>

  <!-- Projects -->
  <section>
    <div class="projects" role="img" aria-label="Blurred photo of a laptop on a wooden desk"></div>
    <div class="projects-tab"></div>
    <div class="projects-tab-mark"></div>
    <h2 class="projects-heading">Project &amp; Work</h2>

    <svg class="slide-arrow" style="left:150px;top:1222px" viewBox="0 0 22 34"><polyline points="18,2 5,17 18,32" fill="none" stroke="#ffffff" stroke-width="2"/></svg>
    <svg class="slide-arrow" style="left:1030px;top:1222px" viewBox="0 0 22 34"><polyline points="4,2 17,17 4,32" fill="none" stroke="#ffffff" stroke-width="2"/></svg>

    <svg class="project-row" width="810" height="195" viewBox="0 0 810 195" role="img" aria-label="Four website project screenshots in hexagon frames">
      <defs>
        <linearGradient id="project-dark" x1="0" y1="0" x2="0" y2="1"><stop offset="0" stop-color="#4a6b8a"/><stop offset="0.35" stop-color="#1b1b1b"/><stop offset="1" stop-color="#0e0e0e"/></linearGradient>
        <linearGradient id="project-pink" x1="0" y1="0" x2="0" y2="1"><stop offset="0" stop-color="#f5c8c8"/><stop offset="1" stop-color="#e08a94"/></linearGradient>
        <linearGradient id="project-light" x1="0" y1="0" x2="0" y2="1"><stop offset="0" stop-color="#2f3a45"/><stop offset="0.25" stop-color="#e9ecef"/><stop offset="1" stop-color="#cfd5da"/></linearGradient>
        <linearGradient id="project-blue" x1="0" y1="0" x2="0" y2="1"><stop offset="0" stop-color="#1e7fd0"/><stop offset="0.4" stop-color="#eef4fa"/><stop offset="1" stop-color="#2a8ad8"/></linearGradient>
      </defs>
      <g stroke="#ffffff" stroke-width="3" stroke-linejoin="round">
        <polygon points="102,4 200,50 200,144 102,190 4,144 4,50" fill="url(#project-dark)"/>
        <polygon points="303,4 401,50 401,144 303,190 205,144 205,50" fill="url(#project-pink)"/>
        <polygon points="504,4 602,50 602,144 504,190 406,144 406,50" fill="url(#project-light)"/>
        <polygon points="705,4 803,50 803,144 705,190 607,144 607,50" fill="url(#project-blue)"/>
      </g>
    </svg>
  </section>

  <!-- Blogs -->
  <section>
    <h2 class="blogs-heading">My Blogs</h2>

    <article class="blog-post" style="left:184px">
      <h3 class="blog-title">Cras a ante vitae enim iaculis aliqu am Mauris nunc quam</h3>
      <p class="blog-excerpt">venenatis nec euismod sit amet egestas placerat est Pellentesque habitant morbi tristique senectus et netus et malesuada fames ac turpis egestas Cras id elit Integer quis urna Ut ante enim dapibus</p>
      <p class="blog-date">Posted 2 day ago</p>
    </article>

    <article class="blog-post" style="left:473px">
      <h3 class="blog-title">Nullam enim leo egestas id condi mentum at laoreet</h3>
      <p class="blog-excerpt">venenatis nec euismod sit amet egestas placerat est Pellentesque habitant morbi tristique senectus et netus et malesuada fames ac turpis egestas Cras id elit Integer quis urna Ut ante enim dapibus</p>
      <p class="blog-date">Posted 2 day ago</p>
    </article>

    <article class="blog-post" style="left:762px">
      <h3 class="blog-title">Duis non nunc Nulla rhoncus dictum metus condime</h3>
      <p class="blog-excerpt">venenatis nec euismod sit amet egestas placerat est Pellentesque habitant morbi tristique senectus et netus et malesuada fames ac turpis egestas Cras id elit Integer quis urna Ut ante enim dapibus</p>
      <p class="blog-date">Posted 2 day ago</p>
    </article>
  </section>

  <!-- Contact -->
  <section>
    <div class="contact" role="img" aria-label="Dark city skyline line illustration behind the contact form"></div>
    <h2 class="contact-heading">CONTACT US</h2>

    <div class="field" style="top:1914px;height:32px">YOUR NAME</div>
    <div class="field" style="top:1953px;height:32px">EMAIL ADDRESS</div>
    <div class="field" style="top:1992px;height:71px">MESSAGE</div>
    <div class="submit-button">SUBMIT</div>

    <div class="contact-line" style="top:1909px">
      <svg width="12" height="16" viewBox="0 0 12 16"><path d="M6 0C2.7 0 0 2.6 0 5.8 0 10 6 16 6 16s6-6 6-10.2C12 2.6 9.3 0 6 0zm0 8.2a2.4 2.4 0 1 1 0-4.8 2.4 2.4 0 0 1 0 4.8z" fill="#ffffff"/></svg>
      <span>417 Larkspur Avenue Suite B12<br>Fernvale, OR 97310</span>
    </div>
    <div class="contact-line" style="top:1967px">
      <svg width="13" height="13" viewBox="0 0 13 13"><path d="M2.6 0.5l2 2.6-1.2 1.6c.8 1.8 2.2 3.2 4 4l1.6-1.2 2.6 2-1.3 2.3C5.4 11.6 1.4 7.6.3 1.8z" fill="#ffffff"/></svg>
      <span>05 31 82 46</span>
    </div>
    <div class="contact-line" style="top:1995px">
      <svg width="14" height="11" viewBox="0 0 14 11"><rect x="0" y="0" width="14" height="11" fill="#ffffff"/><polyline points="0,0 7,6 14,0" fill="none" stroke="#2a2a2a" stroke-width="1.4"/></svg>
      <span>milo@fernleaf-studio.example</span>
    </div>

    <div class="social-row">
      <span class="social-circle"></span>
      <span class="social-circle"></span>
      <span class="social-circle"></span>
      <span class="social-circle"></span>
    </div>
  </section>

  <!-- Footer -->
  <footer class="site-footer"></footer>
  <p class="footer-note">© 2016 Company Name&nbsp; All right reserved&nbsp; Term of Use</p>

</body>
</html>
```